Torvalo PowerPoint Template

I have a company called Torvalo, LLC and my company logo is already designed. I need a PowerPoint template that I will be using to pitch potential investors and business partners. This should be a very professional-looking template that leverages the company logo colors and really pops. The company is an AI product research and development company.

```html
<!DOCTYPE html>
<html lang="en">
<head>
<meta charset="utf-8">
<title>Torvalo – Presentation Template</title>
<link rel="stylesheet" href="https://fonts.googleapis.com/css2?family=Poppins:wght@500;600;700&family=Roboto:wght@300;400;500&display=swap">
<style>
:root{
  --canvas:#a9a9a9;
  --red:#c0152a;
  --red-dark:#8c0a18;
  --ink:#333333;
  --ink-soft:#555555;
  --black:#050505;
  --white:#ffffff;
  --muted:#777777;
}
*{box-sizing:border-box;margin:0;padding:0}
html,body{width:1012px;height:1200px;overflow:hidden;background:var(--canvas)}
body{position:relative;font-family:"Roboto",Arial,sans-serif;color:var(--ink)}
.slide{position:absolute;width:800px;height:450px;transform:scale(.5737);transform-origin:0 0;overflow:hidden;background:var(--white)}
.col-left{left:31.6px}.col-right{left:521px}
.row-1{top:37.9px}.row-2{top:326.4px}.row-3{top:615.6px}.row-4{top:904.1px}
.abs{position:absolute}
.heading{font-family:"Poppins",sans-serif;font-weight:600;color:var(--ink)}
.rule{position:absolute;height:2px;width:56px;background:var(--red)}
.brand{position:absolute;display:flex;align-items:center;gap:9px;font-family:"Poppins",sans-serif;font-weight:600;color:var(--ink);line-height:1}
.brand-dot{border-radius:50%;background:var(--red);flex:none}
.footer-brand{left:25px;top:402px;font-size:27px}
.footer-brand .brand-dot{width:32px;height:32px}
.page-no{position:absolute;right:30px;top:425px;font-size:8px;font-family:"Roboto",sans-serif;color:var(--black)}
.photo{position:absolute}
.body-text{font-size:10.6px;line-height:16.6px;color:var(--ink-soft);text-align:justify}

/* Title */
.cover-top{left:0;top:0;width:800px;height:300px;background:radial-gradient(ellipse at 50% 80%,#d9d9d9 0%,#f1f1f1 45%,#fafafa 80%)}
.cover-brand{left:228px;top:100px;font-size:68px;gap:18px}
.cover-brand .brand-dot{width:74px;height:74px}
.cover-band{left:0;top:300px;width:800px;height:150px;background:var(--black);text-align:center}
.cover-kicker{position:absolute;left:0;right:0;top:22px;font-size:28px;font-weight:300;color:var(--red);letter-spacing:.5px}
.cover-name{position:absolute;left:0;right:0;top:58px;font-family:"Poppins",sans-serif;font-weight:700;font-size:58px;color:var(--white)}

/* Why choose */
.center-title{position:absolute;left:0;right:0;text-align:center;font-size:22px}
.feature{position:absolute;width:170px}
.feature h4{font-family:"Poppins",sans-serif;font-weight:600;font-size:9.5px;color:var(--black);margin-bottom:7px}
.feature p{font-size:8.4px;line-height:14.5px;color:var(--ink-soft)}
.feature.right-al{text-align:right}

/* Agenda */
.agenda-panel{left:0;top:0;width:342px;height:450px;background:linear-gradient(135deg,#2b2b2b 0%,#141414 45%,#333 70%,#0d0d0d 100%)}
.agenda-title{position:absolute;left:110px;top:168px;font-family:"Poppins",sans-serif;font-weight:700;font-size:30px;color:var(--white)}
.agenda-rule{position:absolute;left:120px;top:223px;width:56px;height:2px;background:var(--white)}
.agenda-item{position:absolute;left:312px;display:flex;align-items:center;gap:14px}
.agenda-badge{width:60px;height:60px;border-radius:50%;background:var(--red);border:3px solid var(--white);box-shadow:0 0 0 1px #ddd;display:flex;align-items:center;justify-content:center}
.agenda-item span{font-family:"Poppins",sans-serif;font-weight:600;font-size:9.5px;color:var(--black)}
.top-brand{left:620px;top:20px;font-size:27px}
.top-brand .brand-dot{width:32px;height:32px}

/* Chart */
.legend{position:absolute;left:444px;display:flex;gap:14px;align-items:center}
.legend-badge{width:48px;height:48px;border-radius:50%;border:3px solid var(--red);background:#333;box-shadow:inset 0 0 0 3px #fff;display:flex;align-items:center;justify-content:center;flex:none}
.legend h4{font-family:"Poppins",sans-serif;font-weight:600;font-size:9.3px;color:var(--black);margin-bottom:5px}
.legend p{font-size:7.8px;line-height:12px;color:var(--ink-soft);width:200px}

/* Offer */
.offer-band{left:0;top:0;width:800px;height:172px;background:linear-gradient(160deg,#1a1a1a 0%,#3a3a3a 30%,#0f0f0f 55%,#2e2e2e 80%,#111 100%)}
.offer-stripe{left:0;top:172px;width:800px;height:8px;background:var(--red)}
.offer-card{position:absolute;top:93px;width:158px}
.offer-card .photo{position:relative;width:158px;height:137px;border:2px solid var(--white)}
.offer-card h4{margin-top:10px;text-align:center;font-family:"Roboto",sans-serif;font-weight:500;font-size:12.5px;color:var(--black)}
.offer-card p{margin-top:9px;text-align:center;font-size:7.8px;line-height:12.3px;color:var(--ink-soft)}

/* Thank you */
.thanks-bg{left:0;top:0;width:800px;height:450px;background:radial-gradient(ellipse at 60% 40%,#4a4a4a 0%,#2c2c2c 45%,#1a1a1a 100%)}
.thanks-rule{position:absolute;left:372px;top:168px;width:56px;height:2px;background:#cfcfcf}
.thanks-text{position:absolute;left:0;right:0;top:180px;text-align:center;font-family:"Poppins",sans-serif;font-weight:700;font-size:82px;color:var(--white);line-height:1}
.thanks-text em{font-style:normal;color:var(--red)}
</style>
</head>
<body>

<!-- Cover -->
<section class="slide col-left row-1">
  <div class="abs cover-top" role="img" aria-label="Light grey abstract network of connected points"></div>
  <div class="brand cover-brand"><span class="brand-dot"></span>Torvalo</div>
  <div class="abs cover-band">
    <div class="cover-kicker">INTRODUCTION</div>
    <div class="cover-name">Torvalo, LLC</div>
  </div>
</section>

<!-- Why choose us -->
<section class="slide col-right row-1">
  <h2 class="heading center-title" style="top:28px">Why Choose Us?</h2>
  <div class="rule" style="left:372px;top:71px"></div>
  <svg class="abs" style="left:270px;top:100px" width="260" height="260" viewBox="0 0 260 260">
    <circle cx="130" cy="130" r="128" fill="var(--red)"/>
    <circle cx="130" cy="130" r="114" fill="#fff"/>
  </svg>
  <div class="photo" role="img" aria-label="Humanoid AI figure with glowing circuitry on dark blue background" style="left:291px;top:121px;width:218px;height:218px;border-radius:50%;background:radial-gradient(circle at 60% 45%,#2f4f6f 0%,#142436 50%,#070d16 100%)"></div>
  <div class="feature right-al" style="left:50px;top:73px"><h4>Lorem ipsum dolor sit</h4><p>Lorem ipsum dolor sit amet, consect etur adipiscing elit, sed do eiusmod dolore magna aliqua.</p></div>
  <div class="feature right-al" style="left:50px;top:143px"><h4 style="margin-bottom:22px">Lorem ipsum dolor sit</h4><p>Lorem ipsum dolor sit amet, consect etur adipiscing elit, sed do eiusmod dolore magna aliqua.</p></div>
  <div class="feature" style="left:582px;top:73px"><h4>Lorem ipsum dolor sit</h4><p>Lorem ipsum dolor sit amet, consect etur adipiscing elit, sed do eiusmod dolore magna aliqua.</p></div>
  <div class="feature" style="left:582px;top:143px"><h4>Lorem ipsum dolor sit</h4><p>Lorem ipsum dolor sit amet, consect etur adipiscing elit, sed do eiusmod dolore magna aliqua.</p></div>
  <svg class="abs" style="left:136px;top:75px" width="412" height="100" viewBox="0 0 412 100" fill="none" stroke="#555" stroke-width="1.4">
    <circle cx="10" cy="13" r="6"/><rect x="2" y="22" width="18" height="6" stroke="var(--red)"/>
    <rect x="2" y="84" width="16" height="10"/><path d="M4 84v-6h12v6" stroke="var(--red)"/><circle cx="10" cy="96" r="3"/>
    <circle cx="394" cy="8" r="4"/><path d="M386 22c0-6 16-6 16 0"/><circle cx="388" cy="18" r="3" stroke="var(--red)"/><circle cx="400" cy="18" r="3" stroke="var(--red)"/>
    <rect x="394" y="82" width="14" height="16" rx="2"/><path d="M398 82v-5h6v5" stroke="var(--red)"/>
  </svg>
  <div class="brand footer-brand"><span class="brand-dot"></span>Torvalo</div>
  <div class="page-no">Page No : 05</div>
</section>

<!-- Agenda -->
<section class="slide col-left row-2">
  <div class="abs agenda-panel" role="img" aria-label="Dark grey low-poly geometric texture"></div>
  <div class="agenda-title">Agenda</div>
  <div class="agenda-rule"></div>
  <div class="brand top-brand"><span class="brand-dot"></span>Torvalo</div>
  <div class="agenda-item" style="top:64px"><div class="agenda-badge"><svg width="28" height="28" viewBox="0 0 28 28" fill="none" stroke="#fff" stroke-width="1.5"><circle cx="11" cy="16" r="6"/><circle cx="11" cy="16" r="2"/><circle cx="20" cy="8" r="4"/></svg></div><span>Lorem ipsum dolor sit</span></div>
  <div class="agenda-item" style="top:152px"><div class="agenda-badge"><svg width="28" height="28" viewBox="0 0 28 28" fill="none" stroke="#fff" stroke-width="1.5"><rect x="5" y="5" width="18" height="14" rx="2"/><path d="M8 23h12M10 12h8"/></svg></div><span>Lorem ipsum dolor sit</span></div>
  <div class="agenda-item" style="top:240px"><div class="agenda-badge"><svg width="28" height="28" viewBox="0 0 28 28" fill="none" stroke="#fff" stroke-width="1.5"><circle cx="14" cy="11" r="6"/><path d="M8 24v-5h12v5"/></svg></div><span>Lorem ipsum dolor sit</span></div>
  <div class="agenda-item" style="top:327px"><div class="agenda-badge"><svg width="28" height="28" viewBox="0 0 28 28" fill="none" stroke="#fff" stroke-width="1.5"><path d="M5 24V12l6 4V8l6 4v12zM19 24V6h4v18"/></svg></div><span>Lorem ipsum dolor sit</span></div>
  <div class="page-no">Page No : 02</div>
</section>

<!-- Chart -->
<section class="slide col-right row-2">
  <h2 class="heading center-title" style="top:28px">Chart</h2>
  <div class="rule" style="left:372px;top:71px"></div>
  <svg class="abs" style="left:0;top:0" width="420" height="380" viewBox="0 0 420 380" font-family="Roboto, sans-serif" font-size="7.5" fill="#444">
    <defs>
      <linearGradient id="barDark" x1="0" y1="0" x2="0" y2="1"><stop offset="0" stop-color="#2b2b2b"/><stop offset="1" stop-color="#000"/></linearGradient>
      <linearGradient id="barRed" x1="0" y1="0" x2="0" y2="1"><stop offset="0" stop-color="#d83246"/><stop offset="1" stop-color="#8c0a18"/></linearGradient>
    </defs>
    <line x1="95" y1="54" x2="95" y2="352" stroke="#bbb"/>
    <line x1="95" y1="352" x2="397" y2="352" stroke="#bbb"/>
    <g text-anchor="end">
      <text x="82" y="355">0</text><text x="82" y="330">1</text><text x="82" y="305">2</text><text x="82" y="280">3</text><text x="82" y="255">4</text><text x="82" y="230">5</text><text x="82" y="205">6</text><text x="82" y="180">7</text><text x="82" y="155">8</text><text x="82" y="130">9</text><text x="82" y="105">10</text>
    </g>
    <rect x="117" y="239.5" width="18" height="112.5" fill="url(#barDark)"/>
    <rect x="165" y="227" width="18" height="125" fill="url(#barRed)"/>
    <rect x="213" y="174.5" width="18" height="177.5" fill="url(#barDark)"/>
    <rect x="261" y="227" width="18" height="125" fill="url(#barRed)"/>
    <rect x="309" y="239.5" width="18" height="112.5" fill="url(#barDark)"/>
    <rect x="356" y="174.5" width="18" height="177.5" fill="url(#barRed)"/>
    <g text-anchor="middle">
      <text x="126" y="233">4.5%</text><text x="174" y="220">5%</text><text x="222" y="168">7.1%</text><text x="270" y="220">5%</text><text x="318" y="233">4.5%</text><text x="365" y="168">7.1%</text>
      <text x="126" y="365">2000</text><text x="174" y="365">2005</text><text x="222" y="365">2010</text><text x="270" y="365">2015</text><text x="318" y="365">2020</text><text x="365" y="365">2024</text>
    </g>
  </svg>
  <div class="legend" style="top:97px"><div class="legend-badge"><svg width="20" height="20" viewBox="0 0 20 20" fill="none" stroke="#fff" stroke-width="1.2"><circle cx="10" cy="6" r="3"/><path d="M3 17c0-5 14-5 14 0"/></svg></div><div><h4>Lorem ipsum dolor sit amet</h4><p>Lorem ipsum dolor sit amet, consectetur adipiscing elit, sed do eiusmod tempor incididunt ut</p></div></div>
  <div class="legend" style="top:169px"><div class="legend-badge"><svg width="20" height="20" viewBox="0 0 20 20" fill="none" stroke="#fff" stroke-width="1.2"><circle cx="10" cy="10" r="6"/><circle cx="10" cy="10" r="2"/></svg></div><div><h4>Lorem ipsum dolor sit amet</h4><p>Lorem ipsum dolor sit amet, consectetur adipiscing elit, sed do eiusmod tempor incididunt ut</p></div></div>
  <div class="legend" style="top:242px"><div class="legend-badge"><svg width="20" height="20" viewBox="0 0 20 20" fill="none" stroke="#fff" stroke-width="1.2"><rect x="4" y="5" width="12" height="10" rx="2"/><path d="M7 10h6"/></svg></div><div><h4>Lorem ipsum dolor sit amet</h4><p>Lorem ipsum dolor sit amet, consectetur adipiscing elit, sed do eiusmod tempor incididunt ut</p></div></div>
  <div class="legend" style="top:314px"><div class="legend-badge"><svg width="20" height="20" viewBox="0 0 20 20" fill="none" stroke="#fff" stroke-width="1.2"><circle cx="10" cy="10" r="7"/><circle cx="10" cy="10" r="3"/></svg></div><div><h4>Lorem ipsum dolor sit amet</h4><p>Lorem ipsum dolor sit amet, consectetur adipiscing elit, sed do eiusmod tempor incididunt ut</p></div></div>
  <div class="brand footer-brand"><span class="brand-dot"></span>Torvalo</div>
  <div class="page-no">Page No : 06</div>
</section>

<!-- About -->
<section class="slide col-left row-3">
  <h2 class="heading abs" style="left:55px;top:48px;font-size:22px">About Us</h2>
  <div class="rule" style="left:55px;top:88px"></div>
  <div class="abs body-text" style="left:55px;top:106px;width:313px">
    <p>Lorem ipsum dolor sit amet, consectetur adipiscing elit, sed do eiusmod tempor incididunt ut labore et dolore magna aliqua. Ut enim ad minim veniam, quis nostrud exercitation ullamco laboris nisi ut aliquip ex ea commodo consequat. Duis aute irure dolor in reprehenderit in voluptate velit esse cillum dolore eu fugiat nulla pariatur. Excepteur sint occaecat cupidatat non proident, sunt in culpa qui officia deserunt mollit anim id est laborum.</p>
    <p style="margin-top:16px">Lorem ipsum dolor sit amet, consectetur adipiscing elit, sed do eiusmod tempor incididunt ut labore et dolore magna aliqua. Ut enim ad minim veniam, quis nostrud exercitation ullamco laboris nisi ut aliquip ex ea commodo consequat. Duis aute irure dolor in reprehenderit in voluptate velit esse cillum dolore eu fugiat nulla pariatur.</p>
  </div>
  <svg class="abs" style="left:415px;top:35px" width="350" height="350" viewBox="0 0 350 350"><circle cx="175" cy="175" r="174" fill="none" stroke="var(--red)" stroke-width="1.2"/></svg>
  <div class="photo" role="img" aria-label="Professional working with a laptop and phone in a blue-lit tech office" style="left:420px;top:40px;width:340px;height:340px;border-radius:50%;background:radial-gradient(circle at 70% 40%,#c9d7ea 0%,#6d8fc0 35%,#2a4f86 65%,#0e2346 100%)"></div>
  <div class="photo" role="img" aria-label="Red-tinted technology detail" style="left:538px;top:156px;width:104px;height:104px;border-radius:50%;border:3px solid #fff;background:radial-gradient(circle,#a0182b 0%,#5a0a14 100%)"></div>
  <div class="brand footer-brand"><span class="brand-dot"></span>Torvalo</div>
  <div class="page-no">Page No : 03</div>
</section>

<!-- What we offer -->
<section class="slide col-right row-3">
  <div class="abs offer-band" role="img" aria-label="Dark abstract flowing wave texture"></div>
  <div class="abs offer-stripe"></div>
  <h2 class="heading center-title" style="top:28px;color:#fff">What We Offer</h2>
  <div class="rule" style="left:372px;top:71px;background:#fff"></div>
  <div class="offer-card" style="left:65px"><div class="photo" role="img" aria-label="Hand holding a glowing AI hologram" style="background:radial-gradient(circle at 50% 60%,#e07a3a 0%,#1e3a5e 45%,#0a1628 100%)"></div><h4>Lorem ipsum dolor sit</h4><p>Lorem ipsum dolor sit amet, consectetur adipiscing elit, sed do eiusmod tempor incididunt ut labore et dolore magna aliqua. Ut enim ad minim veniam, quis nostrud exercitation ullamco laboris nisi ut aliquip ex ea commodo consequat.</p></div>
  <div class="offer-card" style="left:233px"><div class="photo" role="img" aria-label="Student with a digital network hologram in a library" style="background:radial-gradient(circle at 50% 55%,#dfe7ee 0%,#8fa2b3 45%,#4b5968 100%)"></div><h4>Lorem ipsum dolor sit</h4><p>Lorem ipsum dolor sit amet, consectetur adipiscing elit, sed do eiusmod tempor incididunt ut labore et dolore magna aliqua. Ut enim ad minim veniam, quis nostrud exercitation ullamco laboris nisi ut aliquip ex ea commodo consequat.</p></div>
  <div class="offer-card" style="left:401px"><div class="photo" role="img" aria-label="Hands typing on a laptop with teal AI interface overlay" style="background:radial-gradient(circle at 40% 55%,#3fa7a0 0%,#174a50 45%,#0a1c22 100%)"></div><h4>Lorem ipsum dolor sit</h4><p>Lorem ipsum dolor sit amet, consectetur adipiscing elit, sed do eiusmod tempor incididunt ut labore et dolore magna aliqua. Ut enim ad minim veniam, quis nostrud exercitation ullamco laboris nisi ut aliquip ex ea commodo consequat.</p></div>
  <div class="offer-card" style="left:569px"><div class="photo" role="img" aria-label="Robotic hand holding a glowing AI chip" style="background:radial-gradient(circle at 55% 35%,#4a8fe0 0%,#173d7a 45%,#071731 100%)"></div><h4>Lorem ipsum dolor sit</h4><p>Lorem ipsum dolor sit amet, consectetur adipiscing elit, sed do eiusmod tempor incididunt ut labore et dolore magna aliqua. Ut enim ad minim veniam, quis nostrud exercitation ullamco laboris nisi ut aliquip ex ea commodo consequat.</p></div>
  <div class="brand footer-brand"><span class="brand-dot"></span>Torvalo</div>
  <div class="page-no">Page No : 07</div>
</section>

<!-- Text page -->
<section class="slide col-left row-4">
  <h2 class="heading abs" style="left:55px;top:48px;font-size:22px">Title Here</h2>
  <div class="rule" style="left:55px;top:88px"></div>
  <div class="abs body-text" style="left:55px;top:106px;width:321px">
    <p>Lorem ipsum dolor sit amet, consectetur adipiscing elit, sed do eiusmod tempor incididunt ut labore et dolore magna aliqua. Ut enim ad minim veniam, quis nostrud exercitation ullamco laboris nisi ut aliquip ex ea commodo consequat.</p>
    <p style="margin-top:16px">Duis aute irure dolor in reprehenderit in voluptate velit esse cillum dolore eu fugiat nulla pariatur. Excepteur sint occaecat cupidatat non proident, sunt in culpa qui officia deserunt mollit anim id est laborum. Lorem ipsum dolor sit amet, consectetur adipiscing elit, sed do eiusmod tempor incididunt ut labore et dolore magna aliqua. Ut enim ad minim veniam, quis nostrud exercitation ullamco laboris nisi ut aliquip ex ea commodo consequat. Duis aute irure dolor in reprehenderit in voluptate velit esse cillum dolore eu fugiat nulla pariatur.</p>
  </div>
  <div class="abs body-text" style="left:422px;top:106px;width:321px">
    <p>Lorem ipsum dolor sit amet, consectetur adipiscing elit, sed do eiusmod tempor incididunt ut labore et dolore magna aliqua. Ut enim ad minim veniam, quis nostrud exercitation ullamco laboris nisi ut aliquip ex ea commodo consequat.</p>
    <p style="margin-top:16px">Duis aute irure dolor in reprehenderit in voluptate velit esse cillum dolore eu fugiat nulla pariatur. Excepteur sint occaecat cupidatat non proident, sunt in culpa qui officia deserunt mollit anim id est laborum. Lorem ipsum dolor sit amet, consectetur adipiscing elit, sed do eiusmod tempor incididunt ut labore et dolore magna aliqua. Ut enim ad minim veniam, quis nostrud exercitation ullamco laboris nisi ut aliquip ex ea commodo consequat. Duis aute irure dolor in reprehenderit in voluptate velit esse cillum dolore eu fugiat nulla pariatur.</p>
  </div>
  <div class="brand footer-brand"><span class="brand-dot"></span>Torvalo</div>
  <div class="page-no">Page No : 04</div>
</section>

<!-- Thank you -->
<section class="slide col-right row-4">
  <div class="abs thanks-bg" role="img" aria-label="Darkened photo of hands working on a laptop"></div>
  <div class="thanks-rule"></div>
  <div class="thanks-text">Thank <em>You</em></div>
</section>

</body>
</html>
```